I need graphics or illustrations to be used in a book and a power point presentation

I have created nine simple graphics using MS paint that were in blog articles. I now need to put these graphics in a book that I am publishing and also in a power point presentation.

I want these graphics to look more professional and consistent looking.

I have provided a word doc showing these graphics that need to be re-done

```html
<!DOCTYPE html>
<html lang="en">
<head>
<meta charset="utf-8">
<title>The true doctrines are taken away after the fulness is rejected</title>
<link rel="stylesheet" href="https://fonts.googleapis.com/css2?family=Fira+Sans+Condensed:wght@400;600;700&display=swap">
<style>
  :root {
    --bg: #dbe7cd;
    --frame: #6f7a66;
    --title: #1c4f8f;
    --ink: #1f1f1a;
    --header: #ecbf4c;
    --line: #df9f2c;
    --cell: #ffffff;
    --total: #fff27a;
    --pill: #fdf3ad;
    --pill-edge: #2a2618;
    --alert: #c8102e;
    --sun: #ffe600;
  }
  * { margin: 0; padding: 0; box-sizing: border-box; }
  html, body { width: 1200px; height: 901px; overflow: hidden; background: var(--bg); }
  body { font-family: "Fira Sans Condensed", "Arial Narrow", sans-serif; color: var(--ink); }
  .chart { position: relative; width: 1200px; height: 901px; background: var(--bg); border: 1px solid var(--frame); }
  .chart-title {
    position: absolute; top: 72px; left: 0; width: 100%;
    text-align: center; color: var(--title); font-weight: 700;
    font-size: 47px; line-height: 52px; letter-spacing: -0.2px;
  }
  .cell { position: absolute; border: 1px solid var(--line); }
  .head {
    background: var(--header); display: flex; align-items: center; justify-content: center;
    font-weight: 700; font-size: 24px;
  }
  .body {
    background: var(--cell); display: flex; flex-direction: column; justify-content: flex-end;
    align-items: center; text-align: center; padding-bottom: 12px;
  }
  .church { font-weight: 700; font-size: 24px; line-height: 31px; }
  .revelations { font-size: 19px; line-height: 26px; margin-top: 2px; }
  .total {
    background: var(--total); display: flex; align-items: center; justify-content: center;
    font-weight: 700; font-size: 29px;
  }
  .total-date { background: var(--header); font-size: 22px; }
  .plus { position: absolute; font-weight: 700; font-size: 24px; transform: translate(-50%, -50%); }
  .pill {
    position: absolute; background: var(--pill); border: 2px solid var(--pill-edge);
    border-radius: 12px; display: flex; align-items: center; justify-content: center;
    text-align: center; font-weight: 700; font-size: 24px; line-height: 30px;
  }
  .alert-band {
    position: absolute; background: var(--alert); color: #fff; font-weight: 700;
    font-size: 24px; display: flex; align-items: center; justify-content: center;
  }
  .sun {
    position: absolute; left: 1070px; top: 626px; width: 106px; height: 106px;
    border-radius: 50%; background: var(--sun);
  }
  .sun-label {
    position: absolute; left: 912px; top: 652px; width: 195px; height: 53px;
    display: flex; align-items: center; justify-content: center;
    font-weight: 700; font-size: 29px;
  }
  .caption { position: absolute; text-align: center; font-size: 24px; line-height: 31px; }
  .caption strong { display: block; font-weight: 700; font-size: 26px; }
  .caption .lead { display: block; }
</style>
</head>
<body>
<main class="chart">
  <h1 class="chart-title">The true doctrines are taken away<br>after the fulness is rejected</h1>

  <!-- First period -->
  <div class="cell head" style="left:79px;top:200px;width:197px;height:90px;">March 1829</div>
  <div class="cell head" style="left:275px;top:200px;width:195px;height:90px;">June 1831</div>
  <div class="cell head" style="left:469px;top:200px;width:196px;height:90px;">December 1834</div>

  <div class="cell body" style="left:79px;top:289px;width:197px;height:314px;">
    <div class="church">Fellowship<br>of<br>Light</div><div class="revelations">47 Revelations</div>
  </div>
  <div class="cell body" style="left:275px;top:289px;width:195px;height:314px;">
    <div class="church">Assembly<br>of<br>Zion</div><div class="revelations">7 Revelations</div>
  </div>
  <div class="cell body" style="left:469px;top:289px;width:196px;height:314px;">
    <div class="church">Society<br>of Latter Day<br>Believers</div><div class="revelations">6 Revelations</div>
  </div>

  <div class="pill" style="left:288px;top:307px;width:170px;height:128px;">Fulness of<br>the Gospel<br>Rejected</div>
  <div class="pill" style="left:482px;top:307px;width:171px;height:153px;">Preparatory<br>Gospel of<br>Abraham<br>Restored</div>

  <div class="cell total" style="left:79px;top:602px;width:197px;height:103px;">2 Years</div>
  <div class="cell total" style="left:275px;top:602px;width:195px;height:103px;">3 1/2 Years</div>
  <div class="cell total" style="left:469px;top:602px;width:196px;height:103px;">2 Years</div>
  <span class="plus" style="left:264px;top:656px;">+</span>
  <span class="plus" style="left:482px;top:656px;">+</span>

  <!-- Later period -->
  <div class="cell head" style="left:716px;top:200px;width:197px;height:90px;">September 1836</div>
  <div class="cell head" style="left:912px;top:200px;width:195px;height:90px;">January 1841</div>
  <div class="alert-band" style="left:716px;top:289px;width:391px;height:44px;">"All Flesh has become corrupt..."</div>

  <div class="cell body" style="left:716px;top:332px;width:197px;height:271px;">
    <div class="church">Society<br>of the Restored<br>Covenant of<br>Believers</div><div class="revelations">11 Revelations</div>
  </div>
  <div class="cell body" style="left:912px;top:332px;width:195px;height:271px;">
    <div class="church">Society of<br>the Restored<br>Covenant of<br>Believers</div><div class="revelations">3 Revelations</div>
  </div>
  <div class="pill" style="left:924px;top:350px;width:170px;height:77px;">Reformation<br>Rejection</div>

  <div class="cell total" style="left:716px;top:602px;width:197px;height:103px;">4 Years</div>
  <div class="cell total total-date" style="left:912px;top:602px;width:195px;height:51px;">June 1844</div>
  <div class="cell total" style="left:912px;top:652px;width:195px;height:53px;"></div>
  <div class="sun" role="img" aria-label="Bright yellow sun marking June 1844"></div>
  <div class="sun-label">3 1/2 Years</div>
  <span class="plus" style="left:730px;top:656px;">+</span>
  <span class="plus" style="left:892px;top:676px;">+</span>

  <!-- Captions -->
  <div class="caption" style="left:172px;top:715px;width:400px;">
    <strong>True and Undefiled<br>Doctrines of the Kingdom<br>Revealed</strong>
    <span class="lead">During the Kirtland Stronghold</span>
  </div>
  <div class="caption" style="left:672px;top:715px;width:480px;">
    <strong>True and Undefiled<br>Doctrines Transfigured</strong>
    <span class="lead">"...from them shall be taken away even<br>that which they have" (2nd Nephi 28:30)</span>
  </div>
</main>
</body>
</html>
```